Research Flier

I need to take a very bad flier that I made and turn it into an amazing flyer for my research group to be shared at a high profile conference.

```html
<!DOCTYPE html>
<html lang="en">
<head>
<meta charset="utf-8">
<title>The Kindred Lab – Research Flier</title>
<link href="https://fonts.googleapis.com/css2?family=Montserrat:wght@600;700;800&family=Roboto:wght@300;400;500;700&display=swap" rel="stylesheet">
<style>
:root{
  --orange:#d9501e;
  --orange-deep:#c9441a;
  --amber:#c99a2e;
  --green:#8dc153;
  --panel-green:#eef3dd;
  --panel-pink:#fce3dc;
  --panel-grey:#f2f2f2;
  --peach:#f2c3a9;
  --ink:#2b2b2b;
  --ink-soft:#4a4a4a;
  --stage:#c9c9c9;
  --white:#ffffff;
}
*{box-sizing:border-box;margin:0;padding:0}
html,body{width:1200px;height:1003px;overflow:hidden}
body{background:var(--stage);font-family:"Roboto",Arial,sans-serif;color:var(--ink);position:relative}
.page{position:absolute;top:166px;width:474px;height:671px;background:var(--white);overflow:hidden}
.page--front{left:88px}
.page--back{left:639px}
.bg-art{position:absolute;inset:0;width:100%;height:100%}
.abs{position:absolute}
.page-title{font-family:"Montserrat",Arial,sans-serif;font-weight:800;color:var(--white);letter-spacing:-.5px;text-shadow:1px 2px 3px rgba(0,0,0,.35)}
.front-title{left:23px;top:30px;font-size:30px}
.back-title{left:34px;top:28px;font-size:21.5px;font-weight:800;text-shadow:1px 1px 2px rgba(0,0,0,.2)}
.section-head{font-family:"Montserrat",Arial,sans-serif;font-weight:700;color:var(--orange);font-size:14.5px;line-height:1;border-left:2px solid var(--green);padding-left:4px}
.photo{position:absolute;background:linear-gradient(135deg,#c7352b,#e36c5c 45%,#f1d9a6);}
.photo--group{background:linear-gradient(135deg,#9bb6cf,#e8d3c0 50%,#7d8fb0)}
.ticks{list-style:none}
.ticks li{position:relative;padding-left:14px;font-size:7.6px;line-height:8.9px;margin-bottom:5px;color:var(--ink)}
.ticks li::before{content:"";position:absolute;left:1px;top:1px;width:7px;height:7px;border-radius:50% 50% 50% 0;background:var(--green);transform:rotate(-45deg)}
.sites-panel{position:absolute;left:10px;top:208px;width:474px;height:204px;background:var(--panel-green);border-radius:14px}
.sites-intro{font-size:7.5px;line-height:9.3px}
.site{position:absolute;width:72px;font-size:5.9px;line-height:7.2px;color:var(--ink-soft)}
.site b{display:block;font-weight:700;color:var(--ink);font-size:6.4px;line-height:8px}
.site span{display:block;margin-bottom:2px}
.build-lead{font-size:8.3px;font-weight:500;line-height:9.5px}
.build-list li{font-size:7.8px;line-height:9.5px;padding-left:17px;margin-bottom:6px}
.pillar{position:absolute;width:74px}
.pillar svg{display:block;width:22px;height:22px;margin-bottom:3px}
.pillar h4{font-family:"Montserrat",Arial,sans-serif;font-size:8px;line-height:9.4px;color:var(--orange);font-weight:700;margin-bottom:2px}
.pillar p{font-size:6px;line-height:7.4px;color:var(--ink-soft)}
.divider{position:absolute;width:0;border-left:1px dashed #bcd7a3}
.footer{position:absolute;left:0;bottom:0;width:474px;height:70px;background:var(--orange)}
.footer-tab{position:absolute;left:59px;top:9px;width:358px;height:70px;background:var(--white);border-radius:30px 30px 0 0}
.org{position:absolute;left:36px;top:12px;display:flex;align-items:flex-start;gap:5px}
.org-dot{width:18px;height:18px;border-radius:50%;background:#2f6fb8;flex:none;margin-top:2px}
.org-text{font-size:5.6px;line-height:6.8px;color:#555;font-weight:300}
.org-text strong{display:block;font-weight:400;font-size:6.6px;color:#333;margin-top:6px;letter-spacing:.3px}
.program{position:absolute;left:176px;top:11px;display:flex;align-items:flex-start;gap:5px}
.program-dot{width:16px;height:16px;border-radius:50%;background:var(--orange);margin-top:4px}
.program-name{font-family:"Roboto",Arial,sans-serif;font-weight:400;font-size:13px;letter-spacing:.6px;color:#333;line-height:15px}
.program-url{font-size:5.5px;color:var(--orange);margin-top:2px;letter-spacing:.2px}
.research-mark{position:absolute;left:303px;top:9px;padding-left:8px;border-left:1px solid #999;text-align:center}
.research-mark i{display:block;width:14px;height:14px;margin:2px auto 3px;background:#333;border-radius:2px}
.research-mark span{font-size:4.6px;letter-spacing:.4px;color:#333}
/* back page */
.projects{position:absolute;left:32px;top:60px;width:402px;height:226px;border:1.5px solid var(--orange);border-radius:0 0 12px 12px;display:flex;background:var(--white)}
.project{flex:1;padding:10px 10px 0;position:relative}
.project+.project{border-left:1.5px solid var(--orange)}
.project h3{font-family:"Montserrat",Arial,sans-serif;font-size:8.6px;line-height:10.5px;color:var(--orange);font-weight:700;padding-bottom:6px;border-bottom:1.2px solid var(--green);height:43px}
.project p{font-size:7px;line-height:9px;color:var(--ink-soft);font-weight:300;margin-top:8px}
.app-shots{position:absolute;left:14px;top:112px;width:105px;height:85px;border-radius:6px;background:linear-gradient(120deg,#eceff2,#cfd6de 60%,#f5f5f5)}
.dims{position:absolute;left:10px;top:114px;width:112px;font-size:3.4px;color:#333;text-align:center}
.dims-grid{display:grid;grid-template-columns:repeat(3,1fr);row-gap:8px;margin-top:3px}
.dims-grid div i{display:block;width:11px;height:11px;border-radius:50%;margin:0 auto 2px;border:2px solid #1d2b4a}
.dims-grid div i.solid{background:#1d2b4a}
.dims-head{display:grid;grid-template-columns:repeat(3,1fr);font-weight:700;border-bottom:.5px solid #333;padding-bottom:1px}
.dims-title{font-weight:700;font-size:3.8px}
.card{position:absolute;border-radius:14px;padding:14px 13px}
.card--areas{left:32px;top:291px;width:217px;height:146px;background:var(--panel-green)}
.card--team{left:253px;top:291px;width:181px;height:146px;background:var(--panel-pink)}
.card h3{font-family:"Montserrat",Arial,sans-serif;color:var(--orange);font-weight:700;font-size:13.5px;line-height:14.5px;margin-bottom:7px}
.card p{font-size:7.6px;line-height:10.2px;margin-bottom:3px}
.card--team p{margin-top:10px}
.pubs{position:absolute;left:32px;top:443px;width:402px;height:162px;background:var(--panel-grey);border-radius:12px 12px 0 0;padding:8px 8px 0 11px;display:flex;gap:9px}
.pubs-col{flex:1;font-size:5.6px;line-height:7.3px;color:#444}
.pubs-col p{margin-bottom:4px}
.pubs-col b{color:#222;font-weight:700}
.pubs h3{font-family:"Montserrat",Arial,sans-serif;font-size:8.4px;color:var(--orange);font-weight:700;margin:9px 0 3px}
</style>
</head>
<body>

<!-- FRONT PAGE -->
<section class="page page--front">
  <svg class="bg-art" viewBox="0 0 474 671" preserveAspectRatio="none" aria-hidden="true">
    <defs>
      <linearGradient id="frontHead" x1="0" y1="0" x2="1" y2="0">
        <stop offset="0" stop-color="#d9501e"/>
        <stop offset=".55" stop-color="#c99a2e"/>
        <stop offset="1" stop-color="#8dc153"/>
      </linearGradient>
    </defs>
    <path d="M0 0H474V40C380 30 300 40 230 52C150 64 70 72 0 78Z" fill="url(#frontHead)"/>
    <path d="M250 60C330 40 420 40 474 70" fill="none" stroke="#8dc153" stroke-width="6" opacity=".8"/>
    <path d="M260 70C330 120 350 220 474 300" fill="none" stroke="#f2c3a9" stroke-width="46" opacity=".75"/>
    <path d="M300 78C360 120 380 210 474 255" fill="none" stroke="#f7dccd" stroke-width="18" opacity=".6"/>
  </svg>

  <h1 class="page-title front-title abs">THE KINDRED LAB</h1>

  <div class="photo" style="left:349px;top:66px;width:125px;height:81px" role="img" aria-label="Photo of students in red uniforms gathered around a table in a classroom"></div>
  <div class="photo photo--group" style="left:349px;top:148px;width:125px;height:81px" role="img" aria-label="Photo of a teacher group holding certificates"></div>

  <h2 class="section-head abs" style="left:23px;top:88px">MISSION</h2>
  <ul class="ticks abs" style="left:29px;top:107px;width:280px">
    <li>Supporting the development of the evidence-based, HEART Learning program and CKT for Educators by assessing program implementation and examining feasibility, impact, and long-term sustainability at the school, district, city, and national levels.</li>
    <li>Developing effective tools and measures to CKT and HEART Learning</li>
    <li>Support global dissemination through impactful manualization</li>
    <li>Contribute to compassion-based education studies worldwide through scientific advancements that examine compassion, common humanity, wellbeing, interdependence, and secular ethics.</li>
  </ul>

  <div class="sites-panel"></div>
  <h2 class="section-head abs" style="left:23px;top:221px">RESEARCH SITES</h2>
  <p class="sites-intro abs" style="left:29px;top:237px;width:340px">We collaborate with global affiliates to conduct collaborative region-specific research.<br>Read below to discover the impactful projects from our worldwide network!</p>

  <div class="site" style="left:29px;top:262px"><b>USA</b><span>Several Studies of Late Elementary and Middle</span><span>Multiple School Districts</span><span>Implementation, RCT, Quasi-experimental, Qualitative, and Mixed Methods</span></div>
  <div class="site" style="left:116px;top:262px"><b>Sweden</b><span>Late Elementary</span><span>2 Schools</span><span>Feasibility &amp; Qualitative Impact Study</span></div>
  <div class="site" style="left:186px;top:262px;width:60px"><b>Spain</b><span>Late Elementary</span><span>Multiple Schools Across Two Regions</span><span>Implementation Study</span></div>
  <div class="site" style="left:249px;top:262px;width:62px"><b>Ukraine</b><span>Teachers</span><span>Feasibility &amp; Qualitative Impact Study</span></div>
  <div class="site" style="left:315px;top:262px;width:66px"><b>Mongolia</b><span>Late Elementary to High School</span><span>800 + Students</span><span>6 Schools</span><span>Implementation study</span></div>
  <div class="site" style="left:384px;top:262px;width:62px"><b>Mexico</b><span>Pre-service Course Study</span><span>Feasibility and Preliminary Impact</span></div>

  <div class="site" style="left:29px;top:330px"><b>Columbia</b><span>Late Elementary</span><span>300+ students</span><span>Implementation Study</span><span>Feasibility &amp; Qualitative Impact Study</span></div>
  <div class="site" style="left:116px;top:330px"><b>Brazil</b><span>Late Elementary</span><span>Ten Schools</span><span>Randomized Controlled Trial</span><span>Teachers &amp; Students</span></div>
  <div class="site" style="left:186px;top:330px;width:42px"><b>Kenya</b><span>Late Elementary</span><span>2 Schools</span><span>Feasibility &amp; Qualitative Impact Study</span></div>
  <div class="site" style="left:249px;top:330px;width:62px"><b>India</b><span>Late Elementary</span><span>More than 1300 Students</span><span>Urban and Rural Implementation studies</span><span>Case Studies</span></div>
  <div class="site" style="left:315px;top:330px;width:62px"><b>South Korea</b><span>Elementary</span><span>Implementation Study</span></div>
  <div class="site" style="left:384px;top:330px;width:62px"><b>Vietnam</b><span>Feasibility</span><span>Implementation in Elementary Students</span><span>Preliminary Impact in Elementary School Students</span></div>

  <h2 class="section-head abs" style="left:23px;top:424px;line-height:17px">BUILDING FOR<br>CHANGE</h2>
  <p class="build-lead abs" style="left:29px;top:459px;width:110px">To meaningfully impact change, we have:</p>
  <ul class="ticks build-list abs" style="left:29px;top:486px;width:130px">
    <li>Identified seven critical domains for whole-school implementation sustainment</li>
    <li>Conducted studies on sustainable implementation and its impact on compassionate systems</li>
    <li>Begun work on global implementation frameworks, monitoring guides, and whole-school trainings</li>
  </ul>

  <div class="divider" style="left:241px;top:425px;height:85px"></div>
  <div class="divider" style="left:324px;top:425px;height:85px"></div>
  <div class="divider" style="left:401px;top:425px;height:85px"></div>
  <div class="divider" style="left:324px;top:520px;height:80px"></div>

  <div class="pillar" style="left:167px;top:421px">
    <svg viewBox="0 0 24 24" fill="none" stroke="#333" stroke-width="1.2" aria-hidden="true"><circle cx="12" cy="4" r="2"/><path d="M12 6v6M9 8l3 2 3-2"/><circle cx="6" cy="16" r="1.6"/><circle cx="12" cy="16" r="1.6"/><circle cx="18" cy="16" r="1.6"/><path d="M3 22c0-2 1.5-3 3-3s3 1 3 3M9 22c0-2 1.5-3 3-3s3 1 3 3M15 22c0-2 1.5-3 3-3s3 1 3 3"/></svg>
    <h4>Leadership Development</h4>
    <p>Those in leadership need skills and HEART understanding for implementation to thrive</p>
  </div>
  <div class="pillar" style="left:249px;top:421px;width:72px">
    <svg viewBox="0 0 24 24" fill="none" stroke="#333" stroke-width="1.2" aria-hidden="true"><rect x="4" y="3" width="13" height="18" rx="1"/><path d="M7 8h7M7 12h5M7 16h4"/><path d="M14 17l7-9 1.5 1.2-7 9L14 19z"/></svg>
    <h4>Implementation</h4>
    <p>Take an implementation approach that works for your school based on what works</p>
  </div>
  <div class="pillar" style="left:335px;top:421px;width:64px">
    <svg viewBox="0 0 24 24" fill="none" stroke="#333" stroke-width="1.2" aria-hidden="true"><path d="M13 12l5-5 5 5v9h-10z"/><rect x="16" y="16" width="3" height="5"/><circle cx="7" cy="10" r="5"/><path d="M7 15v6"/></svg>
    <h4>Community Engagement</h4>
    <p>Engaging families and communities creates a shared vision that enhances sustainability</p>
  </div>
  <div class="pillar" style="left:411px;top:421px;width:60px">
    <svg viewBox="0 0 24 24" fill="none" stroke="#333" stroke-width="1.2" aria-hidden="true"><path d="M3 10h4l10-5v14L7 14H3z"/><path d="M6 14l2 6h3l-2-6"/><path d="M20 9v6"/></svg>
    <h4>Student<br>Voice</h4>
    <p>Student voice and inclusion is developing HEART creates opportunities of stronger program impact</p>
  </div>
  <div class="pillar" style="left:167px;top:516px">
    <svg viewBox="0 0 24 24" fill="none" stroke="#333" stroke-width="1.2" aria-hidden="true"><circle cx="5" cy="12" r="2"/><circle cx="19" cy="12" r="2"/><path d="M1 20c0-2.5 2-4 4-4s4 1.5 4 4M15 20c0-2.5 2-4 4-4s4 1.5 4 4"/><path d="M7 6c3-3 7-3 10 0M17 6l0-2.5M17 6l-2.5 0"/></svg>
    <h4>District Initiative Alignment</h4>
    <p>HEART must align with school initiatives as a part of shared goals that are communicated</p>
  </div>
  <div class="pillar" style="left:249px;top:516px;width:72px">
    <svg viewBox="0 0 24 24" fill="none" stroke="#333" stroke-width="1.2" aria-hidden="true"><circle cx="6" cy="4" r="1.8"/><circle cx="12" cy="4" r="1.8"/><circle cx="18" cy="4" r="1.8"/><path d="M4 21V9h4v12M10 21V9h4v12M16 21V9h4v12"/></svg>
    <h4>Adult SEL</h4>
    <p>Those in leadership need skills and HEART understanding for implementation to thrive</p>
  </div>
  <div class="pillar" style="left:335px;top:516px;width:80px">
    <svg viewBox="0 0 24 24" fill="none" stroke="#333" stroke-width="1.2" aria-hidden="true"><circle cx="5" cy="14" r="1.8"/><circle cx="12" cy="14" r="1.8"/><circle cx="19" cy="14" r="1.8"/><path d="M2 22c0-2 1.4-3.5 3-3.5S8 20 8 22M9 22c0-2 1.4-3.5 3-3.5s3 1.5 3 3.5M16 22c0-2 1.4-3.5 3-3.5s3 1.5 3 3.5"/><path d="M9 3h10v6h-6l-3 2V9H9z"/></svg>
    <h4>Communities of Practice</h4>
    <p>Ongoing professional development support creates opportunities and spaces to strengthen educator development</p>
  </div>

  <footer class="footer">
    <div class="footer-tab">
      <div class="org"><span class="org-dot"></span><div class="org-text">Center for<br>Reflective Science and<br>Care-Based Ethics<strong>HALBROOK UNIVERSITY</strong></div></div>
      <div class="program"><span class="program-dot"></span><div><div class="program-name">HEART<br>LEARNING</div><div class="program-url">www.halbrook-research.edu</div></div></div>
      <div class="research-mark"><i></i><span>RESEARCH</span></div>
    </div>
  </footer>
</section>

<!-- BACK PAGE -->
<section class="page page--back">
  <svg class="bg-art" viewBox="0 0 474 671" preserveAspectRatio="none" aria-hidden="true">
    <defs>
      <linearGradient id="backHead" x1="0" y1="0" x2="1" y2="0">
        <stop offset="0" stop-color="#d9501e"/>
        <stop offset=".5" stop-color="#c99a2e"/>
        <stop offset="1" stop-color="#8dc153"/>
      </linearGradient>
    </defs>
    <path d="M0 0H474V300C455 230 430 170 380 140C300 95 150 118 0 145Z" fill="url(#backHead)"/>
    <path d="M420 210C450 240 465 270 474 300" fill="none" stroke="#e4eccb" stroke-width="12"/>
  </svg>

  <h1 class="page-title back-title abs">Assessment Development Projects</h1>

  <div class="projects">
    <article class="project">
      <h3>Digital Assessment:<br>HEART Learning Insight</h3>
      <p>curriculum-based assessment tool being developed in collaboration with Lumora</p>
      <div class="app-shots" role="img" aria-label="Two phone screens showing the digital assessment app"></div>
    </article>
    <article class="project">
      <h3>Developmentally Appropriate Expectations of Change:</h3>
      <p>We are building age-appropriate rubrics that span the K-12 curriculum. They will help teachers understand expected changes in behavior, communication, relationships, and learning.</p>
    </article>
    <article class="project">
      <h3>Assessment Package for Framework-Based Effectiveness:</h3>
      <p>With affiliates, development of an assessment package for effectiveness studies aimed at assessing domain components, specific to our programs.</p>
      <div class="dims">
        <div class="dims-title">DIMENSIONS</div>
        <div class="dims-head"><span>AWARENESS</span><span>COMPASSION</span><span>ENGAGEMENT</span></div>
        <div class="dims-grid">
          <div><i class="solid"></i>Attention &amp; Self-Awareness</div>
          <div><i></i>Self-Compassion</div>
          <div><i></i>Self-Regulation</div>
          <div><i></i>Interpersonal Awareness</div>
          <div><i class="solid"></i>Compassion for Others</div>
          <div><i></i>Relationship Skills</div>
          <div><i></i>Appreciating Interdependence</div>
          <div><i class="solid"></i>Recognizing Common Humanity</div>
          <div><i></i>Community &amp; Global Engagement</div>
        </div>
      </div>
    </article>
  </div>

  <div class="card card--areas">
    <h3>Other Key Areas of Development</h3>
    <p><b>Global Implementation Framework:</b> Establishing a foundation for a monitoring and evaluation approach that is informed and grounded by practices worldwide to better support implementation.</p>
    <p><b>Whole School/System Trainings and Courses:</b> Utilizing theories for comprehensive school-wide and system-wide implementation to address the sustainability of HEART Learning and SEL programs.</p>
  </div>
  <div class="card card--team">
    <h3>Student Team</h3>
    <p>Currently, over 38 undergraduates, masters students, and PhD students from Halbrook and globally have been a part of our student research team.</p>
  </div>

  <div class="pubs">
    <div class="pubs-col">
      <h3>Key Publications</h3>
      <p><b>US:</b> Marlow, T., Deane, R., Holt-Vargas, K.A. (2024). Cultivating compassion in educational settings - evaluating the effectiveness of a compassion-based SEL program in elementary school children in the US. Open Science Reports. In review.</p>
      <p><b>Colombia:</b> Marlow, T., Rivera Solis, A. M., Ortega Lima, C., &amp; Pratt, N. (2024). Resilience and Renewal: Exploring the Role of Social, Emotional, and Ethical Learning in Elementary Schools in Colombia. Global Review of Schooling. In review.</p>
      <p><b>South Korea:</b> Han, J. W., Seo, D. Y., Cho, E. K., Yoon, B. R., Ahn, M., Baek, J. H., &amp; Nam, S. (2024). Building Resilience and Social–Emotional Competencies in Elementary School Students through a Short-Term Intervention Program Based on the HEART Learning Curriculum. Child Growth Review, 9(2), 117.</p>
    </div>
    <div class="pubs-col">
      <p><b>Ukraine:</b> Berin, S., Holovko, O., Tarasyuk, N., Melnyk, O., Savchenko, T., &amp; Marlow, T (2024). The Effects of a School-Based Social-Emotional and Ethical Learning Program on the Well-Being of Ukrainian Classrooms in the Context of War. War and Wellbeing Review. In Review</p>
      <p><b>Brazil:</b> Moreira, G., Duarte, P., Nakano, J., Rocha, N. V., Almeida, E., Teixeira, S., Brandão, F. C., Marlow, T., &amp; Ueda, E. H. (2024). Mental health improvements of a four-week social, emotional and ethical learning training in Brazilian public school teachers. Journal of Applied Teaching Studies. In review.</p>
      <p><b>Mongolia:</b> Batbold, L., Ganzorig, B., Enkhtuya, B., &amp; Marlow, T. (2024). Predicting the happiness and life satisfaction of middle school students by family factors. Family and Learning Letters, 7(3), 212.</p>
      <p><b>Global Integration:</b> Marlow, T., &amp; Linden, S. L. D. (2023). Nurturing positive mental health and wellbeing in educational settings – the BRIDGE model. Public Health Perspectives, 4</p>
    </div>
  </div>

  <footer class="footer">
    <div class="footer-tab">
      <div class="org"><span class="org-dot"></span><div class="org-text">Center for<br>Reflective Science and<br>Care-Based Ethics<strong>HALBROOK UNIVERSITY</strong></div></div>
      <div class="program"><span class="program-dot"></span><div><div class="program-name">HEART<br>LEARNING</div><div class="program-url">www.halbrook-research.edu</div></div></div>
      <div class="research-mark"><i></i><span>RESEARCH</span></div>
    </div>
  </footer>
</section>

</body>
</html>
```